eBook book cover for erotic novel set in Singapore (yes really!)

Hello - here’s a bit of background on my book, along with some thoughts on the cover. I hope this helps; am happy to answer any questions and provide further example chapters if that would help you get a better idea of what it’s all about (some extracts are attached to this brief).

1. "Under Quiet Lanterns" - synopsis
“I'm curious—and tempted. Oh dear!” is Bea’s reply to an advert posted on the internet and she enters into a relationship unlike any other she has experienced before—one that stimulates, frustrates, consumes and ultimately, delights, her.

Owen a successful banker living in Singapore has placed an online invitation for “irregular intimacy” with a “sexy, well-dressed lover with stimulating kinks”. Bea’s feeling dulled by her demanding job and the undemanding social rituals of her life in Singapore: she’s attracted to Owen’s slightly jaded urbanity and quirky ways. He finds her plain-speaking exuberance a refreshing contrast to his own more conservative nature.

After a sparky, and at times, spiky, email exchange they meet at a rooftop bar in Singapore’s Chinatown. Over cocktails they agree the seven rules of their relationship (the first one—“No questions about work or personal lives”). Despite this formality, the sexual attraction between them is intense—as is the sex when they first manage to schedule it. Over subsequent weeks they craft a list of sexual experiences they intend to enjoy together. Once they’ve completed ‘The List’ (on an Excel spreadsheet) they’ll part. That’s the intention anyway.

As their relationship develops they both can’t help applying their controlling corporate selves to their secret life. Apart from the proposed experiences on the agreed list, each of them sometimes introduces new things to surprise the other. Under Quiet Lanterns is set mainly in Singapore—where the exotic sights, sounds and tastes provide a sensual backdrop to the increasingly intense affair.

The novel is about two people who believe they can manage their relationship in the same way they organise everything else in their lives—with closely calibrated calendar entries, tightly planned sexual liaisons and multiple lists. They relish the contrasts between their demanding jobs (the frequent travel, late night conference calls and always-on Quillphones) and indulging their imaginations with someone they trust. Bea begins to appreciate just what being “sex fit” entails. The sex scenes are explicit (“Sex where she did things she couldn’t tell her sisters about”) and driven in part by their competitive natures.

However, it gradually becomes clear that it is becoming harder for them to contain their relationship to just sex, no matter how delightful. They had both originally committed to a ‘no strings attached’ affair but they struggle with their growing feelings for each other. Owen initially drives the relationship but increasingly becomes out of his depth whilst Bea gains confidence. The novel ends with over half The List still to be completed—will they be able to keep to the rules, and more importantly, maintain the expected emotional distance they’ve both agreed to?

2. Cover thoughts
I’d like to avoid the typical cliched image of say, a silk tie and handcuffs, that one often sees on book covers of this genre. A reference to Singapore/Asia would be good of course (an orchid too obvious?), and naturally being an ebook, the cover needs to be simple and striking. I have a second book planned, and half written, and possibly a third. A design that thus lends itself to being adapted slightly so as to support a trilogy would be particularly useful.

3. Author's name
Gus Palmer

Thanks
Gus

Women 25-45

Serif
Decorative
Script

85cae6
3176b5

• A reference to Asia/Singapore
• A sense of the unknown, reference to Asia/Singapore, a hint of sex attraction, reference to corporate life.
• Just had a thought that a single stiletto shoe (on a carpet, wooden floorboards?) might be interesting.
• Be overly explicit sexually - have the usual cliche of a scantily clad woman for example

```html
<!DOCTYPE html>
<html lang="en">
<head>
<meta charset="utf-8">
<title>Under Quiet Lanterns — Cover Wrap</title>
<link rel="stylesheet" href="https://fonts.googleapis.com/css2?family=Bebas+Neue&family=Montserrat:wght@600;800&display=swap">
<style>
  :root {
    --stage: #e6e6e6;
    --paper: #f3f3f3;
    --spine-paper: #ececec;
    --ink-red: #7c0f14;
    --shoe-red: #b3151b;
    --shoe-dark: #5e0a0d;
  }
  * { margin: 0; padding: 0; box-sizing: border-box; }
  html, body { width: 1200px; height: 800px; overflow: hidden; }
  body {
    background: var(--stage);
    display: flex;
    align-items: center;
    justify-content: center;
  }
  .cover-wrap {
    display: flex;
    height: 620px;
    box-shadow: 0 10px 30px rgba(0,0,0,0.12);
  }

  /* Back cover */
  .back-cover {
    width: 410px;
    background: var(--paper);
    padding: 34px 30px 30px;
    display: flex;
    flex-direction: column;
  }
  .back-author {
    font-family: "Montserrat", sans-serif;
    font-weight: 800;
    font-size: 13px;
    letter-spacing: 4px;
    color: var(--ink-red);
    text-align: right;
  }
  .back-title {
    font-family: "Bebas Neue", sans-serif;
    font-weight: 400;
    font-size: 45px;
    line-height: 1;
    color: var(--ink-red);
    text-align: right;
    margin-top: 2px;
  }
  .back-blurb {
    margin-top: 14px;
    font-family: "Montserrat", sans-serif;
    font-weight: 800;
    font-size: 9.6px;
    line-height: 1.32;
    color: var(--ink-red);
    text-align: justify;
    text-align-last: center;
  }
  .back-footer {
    margin-top: auto;
    display: flex;
    justify-content: space-between;
  }
  .back-slot {
    width: 96px;
    height: 60px;
    background: var(--ink-red);
    color: #f3f3f3;
    font-family: "Montserrat", sans-serif;
    font-weight: 600;
    font-size: 8px;
    display: flex;
    align-items: center;
    justify-content: center;
  }
  .back-slot.isbn { width: 102px; height: 66px; }

  /* Spine */
  .spine {
    width: 30px;
    background: var(--spine-paper);
    border-left: 1px solid #dcdcdc;
    border-right: 1px solid #dcdcdc;
    display: flex;
    flex-direction: column;
    align-items: center;
    padding: 22px 0;
  }
  .spine-title, .spine-author {
    writing-mode: vertical-rl;
    color: var(--ink-red);
  }
  .spine-title {
    font-family: "Bebas Neue", sans-serif;
    font-size: 25px;
    letter-spacing: 3px;
  }
  .spine-author {
    margin-top: 36px;
    font-family: "Montserrat", sans-serif;
    font-weight: 800;
    font-size: 9px;
    letter-spacing: 5px;
  }

  /* Front cover */
  .front-cover {
    position: relative;
    width: 410px;
    background: var(--paper);
    overflow: hidden;
  }
  .shoe-art {
    position: absolute;
    left: 262px;
    top: 18px;
    width: 138px;
    height: 236px;
    background: radial-gradient(closest-side at 50% 55%, var(--shoe-red) 0%, var(--shoe-dark) 70%, rgba(243,243,243,0) 100%);
  }
  .front-title {
    position: absolute;
    left: 38px;
    top: 168px;
    font-family: "Bebas Neue", sans-serif;
    font-weight: 400;
    font-size: 104px;
    line-height: 0.9;
    color: var(--ink-red);
  }
  .skyline-art {
    position: absolute;
    left: 0;
    right: 0;
    top: 476px;
    height: 106px;
    background: linear-gradient(to bottom, rgba(124,15,20,0.55), var(--ink-red) 45%);
  }
  .front-author {
    position: absolute;
    left: 0;
    right: 0;
    bottom: 18px;
    text-align: center;
    font-family: "Montserrat", sans-serif;
    font-weight: 800;
    font-size: 13px;
    letter-spacing: 4px;
    color: var(--ink-red);
  }
</style>
</head>
<body>
  <main class="cover-wrap">
    <section class="back-cover">
      <p class="back-author">GUS PALMER</p>
      <h2 class="back-title">UNDER QUIET LANTERNS</h2>
      <p class="back-blurb">Lorem ipsum dolor sit amet, consectetur adipisicing elit, sed do eiusmod tempor incididunt ut labore et dolore magna aliqua. Ut enim ad minim veniam, quis nostrud exercitation. Lorem ipsum dolor sit amet, consectetur adipisicing elit, sed do eiusmod tempor incididunt ut labore et dolore magna aliqua. Ut enim ad minim veniam, quis nostrud exercitation. Lorem ipsum dolor sit amet, consectetur adipisicing elit, sed do eiusmod tempor incididunt ut labore et dolore magna aliqua. Ut enim ad minim veniam, quis nostrud exercitation. Lorem ipsum dolor sit amet, consectetur adipisicing elit, sed do eiusmod tempor incididunt ut labore et dolore magna aliqua. Ut enim ad minim veniam, quis nostrud exercitation. Lorem ipsum dolor sit amet, consectetur adipisicing elit, sed do eiusmod tempor incididunt ut labore et dolore magna aliqua. Ut enim ad minim veniam, quis nostrud exercitation. Lorem ipsum dolor sit amet, consectetur adipisicing elit, sed do eiusmod tempor incididunt ut labore et dolore magna aliqua. Ut enim ad minim veniam, quis nostrud exercitation. Lorem ipsum dolor sit amet, consectetur adipisicing elit, sed do eiusmod tempor incididunt ut labore et dolore magna aliqua. Ut enim ad minim veniam, quis nostrud exercitation. Lorem ipsum dolor sit amet, consectetur adipisicing elit, sed do eiusmod tempor incididunt ut labore et dolore magna aliqua. Ut enim ad minim veniam, quis nostrud exercitation.</p>
      <div class="back-footer">
        <div class="back-slot logo">LOGO</div>
        <div class="back-slot isbn">ISBN</div>
      </div>
    </section>

    <aside class="spine">
      <span class="spine-title">UNDER QUIET LANTERNS</span>
      <span class="spine-author">GUS PALMER</span>
    </aside>

    <section class="front-cover">
      <div class="shoe-art" role="img" aria-label="Glossy red stiletto high-heel shoe"></div>
      <h1 class="front-title">UNDER<br>QUIET<br>LANTERNS</h1>
      <div class="skyline-art" role="img" aria-label="Dark red silhouette of a city skyline"></div>
      <p class="front-author">GUS PALMER</p>
    </section>
  </main>
</body>
</html>
```